White wine label design for a Croatian Winery

We need a wine label design for white wine. The brand of wine is called Vendrak (which means Monastery). The label is rounded around a bottle (there is no front and backside separate). The label has to show 3 or 4 visual elements: monastery, desert, vineyard, and a river. Except for wine name label has to have one more inscription: Podravsko vino iz pustinje (translated to English: wine from the desert) and Bijeli Cuvee (bijeli means white, it's a blend of wine).
The rest of the text that goes on a label will be sent to you after the design is selected.

Target Market(s)

Sales in winery, wine shops and small stores

Requirements
Must have
• 2 variants of Label, one is for the transparent white bottle and the other is for a dark bottle
3 or 4 visual elements: monastery, desert, vineyard, and a river.
The label is rounded around a bottle (there is no front and backside separate).
Text: Vendrak (name of the wine), Podravsko vino iz pustinje (let's say it's a description - it means a wine from a desert), and Bijeli Cuvee (it's a blend of a wine)
Nice to have
• Elegant, fancy/royal, minimalistic style

```html
<!DOCTYPE html>
<html lang="hr">
<head>
<meta charset="utf-8">
<title>Vendrak – Bijeli Cuvee label</title>
<link rel="stylesheet" href="https://fonts.googleapis.com/css2?family=Tinos&family=Pinyon+Script&display=swap">
<style>
  :root {
    --backdrop: #1c1c1c;
    --paper: #f1efe4;
    --ink: #1e1e1e;
    --ornament-tone: #b4b2aa;
    --gold: #b89a52;
    --gold-light: #e3d29c;
    --gold-dark: #8f7535;
    --scene-light: #dcdad0;
    --scene-dark: #77766f;
  }
  * { margin: 0; padding: 0; box-sizing: border-box; }
  html, body {
    width: 1200px;
    height: 1200px;
    overflow: hidden;
    background: var(--backdrop);
  }
  .svg-defs { position: absolute; width: 0; height: 0; }
  .canvas {
    position: relative;
    width: 1200px;
    height: 1200px;
    display: flex;
    align-items: center;
    justify-content: center;
  }
  .label {
    position: relative;
    width: 640px;
    height: 910px;
    display: flex;
    flex-direction: column;
  }
  .zigzag-edge {
    display: block;
    width: 640px;
    height: 22px;
  }
  .zigzag-edge.is-bottom { transform: scaleY(-1); }
  .ornament-band {
    background: var(--paper);
    padding: 4px 0;
    border-top: 3px solid var(--ink);
    border-bottom: 3px solid var(--ink);
  }
  .ornament-band .rule {
    height: 1px;
    background: var(--ink);
  }
  .ornament-band .rosette-strip {
    height: 34px;
    margin: 3px 0;
    background: var(--ornament-tone);
  }
  .label-body {
    flex: 1;
    background: var(--paper);
    display: flex;
    flex-direction: column;
    align-items: center;
  }
  .brand-name {
    margin-top: 64px;
    font-family: "Tinos", serif;
    font-weight: 400;
    font-size: 80px;
    letter-spacing: 5px;
    text-transform: uppercase;
    color: var(--gold);
    line-height: 1;
  }
  .landscape {
    margin-top: 40px;
    width: 564px;
    height: 292px;
    background: linear-gradient(180deg, var(--scene-light) 0%, #b2b0a8 50%, var(--scene-dark) 100%);
  }
  .description {
    margin-top: 44px;
    font-family: "Tinos", serif;
    font-size: 36px;
    color: var(--ink);
    line-height: 1;
  }
  .cuvee {
    margin-top: 24px;
    font-family: "Pinyon Script", cursive;
    font-size: 68px;
    color: var(--ink);
    line-height: 1;
  }
</style>
</head>
<body>
  <svg class="svg-defs" aria-hidden="true">
    <defs>
      <linearGradient id="gold-sheen" x1="0" y1="0" x2="1" y2="0">
        <stop offset="0" stop-color="#8f7535"/>
        <stop offset="0.35" stop-color="#e3d29c"/>
        <stop offset="0.6" stop-color="#b89a52"/>
        <stop offset="1" stop-color="#8f7535"/>
      </linearGradient>
      <pattern id="sawtooth" width="20" height="22" patternUnits="userSpaceOnUse">
        <polygon points="0,22 10,6 20,22" fill="#c9ae68"/>
      </pattern>
    </defs>
  </svg>

  <main class="canvas">
    <section class="label">
      <svg class="zigzag-edge" viewBox="0 0 640 22" aria-hidden="true">
        <rect width="640" height="22" fill="url(#sawtooth)"/>
        <rect y="18" width="640" height="4" fill="url(#gold-sheen)"/>
      </svg>
      <div class="ornament-band">
        <div class="rule"></div>
        <div class="rosette-strip" role="img" aria-label="Ornamental rosette border"></div>
        <div class="rule"></div>
      </div>

      <div class="label-body">
        <h1 class="brand-name">Vendrak</h1>
        <div class="landscape" role="img" aria-label="Engraved landscape of a monastery among vineyard rows with rolling hills"></div>
        <p class="description">Podravsko vino iz pustinje</p>
        <p class="cuvee">Bijeli Cuvee</p>
      </div>

      <div class="ornament-band">
        <div class="rule"></div>
        <div class="rosette-strip" role="img" aria-label="Ornamental rosette border"></div>
        <div class="rule"></div>
      </div>
      <svg class="zigzag-edge is-bottom" viewBox="0 0 640 22" aria-hidden="true">
        <rect width="640" height="22" fill="url(#sawtooth)"/>
        <rect y="18" width="640" height="4" fill="url(#gold-sheen)"/>
      </svg>
    </section>
  </main>
</body>
</html>
```